Real estate investor business card to retire young ;)!

I need a logo design and a business card. I am based in Montreal, Canada. I buy multi-family properties and do lots development. The final design should communicate that I am a problem solver and reliable.

This card will be given to other investors, to potential sellers and industry experts.

Target Market(s)

Real estate community, multi-family owners

Industry/Entity Type

Real Estate Development

Contact Information for Business Card

My name: Karine Beaulac
email: immo.karine.beaulac@postelune.ca
cellphone: (438) 555-2947

Logo Text

Gestion immobilière

Font styles to use
Sans Serif

Colors
3176b5

Requirements
Must have
• Within 1-2 seconds the person who sees my card should know that I buy properties and lot. Areas to for Phone number and email adress. I do not have a business name. The card should simply state my name and what I do. The logo should be remembered by the person who reads my card
Should not have
• Colors too bright. Too much small details. I want something balanced, bold without being agressive.

```html
<!DOCTYPE html>
<html lang="en">
<head>
<meta charset="utf-8">
<title>Karine Beaulac – Business Card</title>
<link rel="stylesheet" href="https://fonts.googleapis.com/css2?family=Roboto:wght@400;700&display=swap">
<style>
  :root {
    --page-bg: #d8d5cf;
    --card-light: #eeeeef;
    --card-shade: #cfd0d4;
    --brand-blue: #1f4a9c;
    --band-blue: #27509f;
    --band-deep: #1a3c84;
    --stripe-grey: #7b7b7f;
    --text-grey: #57575c;
    --name-white: #f4f6fa;
  }
  * { margin: 0; padding: 0; box-sizing: border-box; }
  html, body { width: 1200px; height: 970px; overflow: hidden; }
  body {
    background: var(--page-bg);
    font-family: "Roboto", Arial, sans-serif;
    position: relative;
  }
  .business-card {
    position: absolute;
    left: 100px;
    top: 200px;
    width: 1000px;
    height: 570px;
    background: linear-gradient(160deg, var(--card-light) 0%, #e2e3e6 55%, var(--card-shade) 100%);
    box-shadow: 0 10px 30px rgba(0,0,0,0.18);
    overflow: hidden;
  }
  .roof-shape { position: absolute; inset: 0; width: 1000px; height: 570px; }
  .holder {
    position: absolute;
    left: 60px;
    top: 62px;
    color: var(--name-white);
  }
  .holder-name { font-size: 34px; font-weight: 700; letter-spacing: 0.3px; line-height: 1.1; }
  .holder-role { font-size: 24px; font-weight: 400; line-height: 1.2; }
  .contact {
    position: absolute;
    left: 56px;
    top: 338px;
    color: var(--text-grey);
    font-size: 24px;
    line-height: 1.25;
  }
  .contact-address { margin-bottom: 16px; }
  .contact-line { display: flex; align-items: center; gap: 12px; margin-bottom: 8px; }
  .contact-icon { width: 22px; height: 22px; flex: none; }
  .brand {
    position: absolute;
    right: 62px;
    top: 448px;
    width: 340px;
    text-align: center;
  }
  .brand-name {
    display: flex;
    align-items: center;
    justify-content: center;
    gap: 12px;
    font-weight: 700;
    font-size: 34px;
    line-height: 1.2;
    color: var(--brand-blue);
  }
  .brand-square { width: 18px; height: 18px; background: var(--brand-blue); flex: none; }
  .brand-tagline {
    margin-top: 6px;
    font-size: 18px;
    font-weight: 400;
    color: var(--text-grey);
    letter-spacing: 0.3px;
  }
</style>
</head>
<body>
  <div class="business-card">
    <svg class="roof-shape" viewBox="0 0 1000 570" aria-hidden="true">
      <defs>
        <linearGradient id="bandBlue" x1="0" y1="0" x2="1" y2="0">
          <stop offset="0" stop-color="var(--band-blue)"/>
          <stop offset="0.5" stop-color="var(--band-deep)"/>
          <stop offset="1" stop-color="var(--band-blue)"/>
        </linearGradient>
      </defs>
      <polygon fill="url(#bandBlue)" points="0,0 1000,0 1000,187 705,55 0,233"/>
      <polygon fill="var(--stripe-grey)" points="0,233 705,55 1000,187 1000,252 705,70 0,273"/>
    </svg>

    <div class="holder">
      <div class="holder-name">Karine Beaulac</div>
      <div class="holder-role">Owner</div>
    </div>

    <div class="contact">
      <div class="contact-address">PO BOX 418, rue Saint-Denis<br>Montréal, QC H2X 3K8</div>
      <div class="contact-line">
        <svg class="contact-icon" viewBox="0 0 22 22" aria-hidden="true"><rect x="6" y="2" width="10" height="18" rx="2" fill="none" stroke="var(--brand-blue)" stroke-width="2"/><circle cx="11" cy="16.5" r="1.2" fill="var(--brand-blue)"/></svg>
        <span>(438) 555-2947</span>
      </div>
      <div class="contact-line">
        <svg class="contact-icon" viewBox="0 0 22 22" aria-hidden="true"><rect x="2" y="5" width="18" height="13" fill="var(--brand-blue)"/><polyline points="2,5 11,12 20,5" fill="none" stroke="#fff" stroke-width="1.5"/></svg>
        <span>immo.karine.beaulac@postelune.ca</span>
      </div>
      <div class="contact-line">
        <svg class="contact-icon" viewBox="0 0 22 22" aria-hidden="true"><circle cx="11" cy="11" r="9" fill="var(--brand-blue)"/><g fill="none" stroke="#fff" stroke-width="1"><ellipse cx="11" cy="11" rx="4" ry="9"/><line x1="2" y1="11" x2="20" y2="11"/></g></svg>
        <span>www.beaulac-immo.ca</span>
      </div>
    </div>

    <div class="brand">
      <div class="brand-name">
        <span class="brand-square"></span>
        <span>Karine Beaulac</span>
      </div>
      <div class="brand-tagline">Buying Multi-Family Properties &amp; Lots</div>
    </div>
  </div>
</body>
</html>
```